BrightArc Orthodontics Exterior Signage

We need 4 exterior signs designed for our orthodontics practice based in Sydney, Australia. The signs face busy streets and walkways and experience heavy foot traffic. The existing signage has been in use for about 5 years and is starting to feel outdated. We want the signs to be clean and modern with effective use of brand colours and imagery. For details about the practice and brand style, see: brightarcorthodontics-example.com.au

Target Market(s)

Foot traffic in affluent suburb of Sydney, Australia.

Industry/Entity Type

Health Care

Font styles to use
Sans Serif

Colors

Designer to choose colors to be used in the design.

Requirements
Must have
• Modern, clean, professional feel. Family friendly.
Nice to have
• Effective use of lifestyle imagery. For similar examples, see: https://www.clearvexa-example.com.au
Should not have
• No close-up imagery of teeth or mouths.

```html
<!DOCTYPE html>
<html lang="en">
<head>
<meta charset="utf-8">
<title>BrightArc Orthodontics – Exterior Signage</title>
<link rel="stylesheet" href="https://fonts.googleapis.com/css2?family=Open+Sans:wght@400;600;700&display=swap">
<style>
  :root {
    --green: #3a9479;
    --purple: #6b2a93;
    --purple-deep: #4a1760;
    --blue: #1b9fd9;
    --blue-deep: #0f5680;
    --grey-text: #8a8a8a;
    --white: #ffffff;
    --panel-light: #f4f4f4;
    --panel-grey-a: #9c9c9c;
    --panel-grey-b: #e4e4e4;
  }
  * { box-sizing: border-box; margin: 0; padding: 0; }
  html, body { width: 1200px; height: 800px; overflow: hidden; background: var(--white); }
  body { position: relative; font-family: "Open Sans", Arial, sans-serif; }

  .sign { position: absolute; overflow: hidden; }
  .sign svg.backdrop { position: absolute; inset: 0; width: 100%; height: 100%; }

  .brand-name {
    position: absolute; left: 0; right: 0; text-align: center;
    font-weight: 600; color: var(--purple); white-space: nowrap;
  }

  /* Banner signs */
  .banner { top: 90px; width: 236px; height: 620px; background: linear-gradient(#ffffff, var(--panel-light)); }
  .banner--contact { left: 75px; }
  .banner--slogan { left: 330px; }
  .banner .brand-name { top: 72px; font-size: 18px; }

  .contact-block { position: absolute; left: 0; right: 0; top: 410px; color: var(--white); text-align: center; }
  .contact-name { font-size: 21px; font-weight: 600; line-height: 1.1; }
  .contact-role { font-size: 14px; font-weight: 600; margin-top: 3px; }
  .contact-phone { font-size: 38px; font-weight: 600; margin-top: 6px; letter-spacing: 0.5px; }
  .contact-rule { width: 206px; height: 1px; background: rgba(255,255,255,0.8); margin: 8px auto 0; }
  .contact-web { font-size: 10px; font-weight: 600; margin: 12px 0 13px; }
  .partner { display: flex; align-items: center; justify-content: center; gap: 6px; margin-top: 12px; font-size: 16px; }
  .partner-dot { width: 18px; height: 18px; border-radius: 50%; background: var(--white); }
  .partner-line { font-size: 12px; }

  .slogan-block { position: absolute; left: 16px; top: 464px; color: var(--white); font-weight: 600; }
  .slogan { font-size: 28px; line-height: 1.25; }
  .slogan-arrows { font-size: 24px; letter-spacing: 0.5px; margin-top: 4px; }

  /* Landscape signs */
  .landscape { width: 540px; height: 330px; background: linear-gradient(90deg, var(--panel-grey-a), var(--panel-grey-b)); }
  .landscape--upper { left: 602px; top: 92px; z-index: 1; }
  .landscape--lower { left: 630px; top: 370px; z-index: 2; }
  .landscape .brand-name { left: 180px; right: auto; width: 236px; top: 70px; font-size: 18px; }
  .landscape .tagline {
    position: absolute; left: 180px; width: 236px; top: 96px; text-align: center;
    font-size: 12.5px; font-weight: 700; white-space: nowrap;
  }
  .tagline .lead { color: var(--green); }
  .tagline .rest { color: var(--purple); }

  .portrait {
    position: absolute; border-radius: 50%;
    border: 2px solid rgba(255,255,255,0.85);
  }
  .tone-warm { background: radial-gradient(circle at 50% 40%, #d9b8a0, #7a5a4a 60%, #3c2a24); }
  .tone-sunset { background: radial-gradient(circle at 30% 30%, #f3c27a, #a77a52 55%, #4e3b2c); }
  .tone-garden { background: radial-gradient(circle at 50% 45%, #c7a48c, #3f5a3a 65%, #1f2e1d); }
  .tone-desert { background: radial-gradient(circle at 50% 45%, #dcc6a6, #a79a7a 60%, #6f7058); }
  .tone-studio { background: radial-gradient(circle at 50% 45%, #9a6f58, #e8e8e8 70%, #ffffff); }
</style>
</head>
<body>

<!-- Tall banner: practitioner contact -->
<section class="sign banner banner--contact">
  <svg class="backdrop" viewBox="0 0 236 620" preserveAspectRatio="none">
    <defs>
      <linearGradient id="contactPhoto" x1="0" y1="0" x2="1" y2="1">
        <stop offset="0" stop-color="#b9c2c8"/>
        <stop offset="0.5" stop-color="#6e6660"/>
        <stop offset="1" stop-color="#2e2e33"/>
      </linearGradient>
      <linearGradient id="contactBlue" x1="0" y1="0" x2="1" y2="0">
        <stop offset="0" stop-color="var(--blue)"/>
        <stop offset="1" stop-color="var(--blue-deep)"/>
      </linearGradient>
    </defs>
    <g role="img" aria-label="Lifestyle photo of a smiling young woman outdoors">
      <path d="M0,192 C80,168 170,160 236,128 L236,400 L0,400 Z" fill="url(#contactPhoto)"/>
    </g>
    <path d="M0,380 C120,372 205,310 236,240 L236,620 L0,620 Z" fill="url(#contactBlue)"/>
  </svg>
  <div class="brand-name">brightarc orthodontics</div>
  <div class="contact-block">
    <p class="contact-name">Dr Helena Marsh</p>
    <p class="contact-role">Specialist Orthodontist</p>
    <p class="contact-phone">9000 4417</p>
    <div class="contact-rule"></div>
    <p class="contact-web">brightarcorthodontics-example.com.au</p>
    <div class="contact-rule"></div>
    <div class="partner">
      <span class="partner-dot"></span>
      <span>clearvexa</span>
      <span class="partner-line">| aligned for life</span>
    </div>
  </div>
</section>

<!-- Tall banner: slogan -->
<section class="sign banner banner--slogan">
  <svg class="backdrop" viewBox="0 0 236 620" preserveAspectRatio="none">
    <defs>
      <linearGradient id="sloganPhoto" x1="0" y1="0" x2="1" y2="1">
        <stop offset="0" stop-color="#e6e1dc"/>
        <stop offset="0.55" stop-color="#c8b29c"/>
        <stop offset="1" stop-color="#7d6250"/>
      </linearGradient>
      <linearGradient id="sloganPurple" x1="0" y1="0" x2="1" y2="0">
        <stop offset="0" stop-color="var(--purple)"/>
        <stop offset="1" stop-color="var(--purple-deep)"/>
      </linearGradient>
    </defs>
    <g role="img" aria-label="Lifestyle photo of a laughing couple on a beach">
      <path d="M0,192 C70,150 160,140 236,130 L236,460 L0,460 Z" fill="url(#sloganPhoto)"/>
    </g>
    <path d="M0,460 C110,455 200,400 236,318 L236,620 L0,620 Z" fill="url(#sloganPurple)"/>
  </svg>
  <div class="brand-name">brightarc orthodontics</div>
  <div class="slogan-block">
    <p class="slogan">Creating great,<br>straight smiles</p>
    <p class="slogan-arrows">&gt;&gt;&gt;&gt;&gt;&gt;&gt;&gt;&gt;&gt;&gt;&gt;&gt;</p>
  </div>
</section>

<!-- Landscape sign: upper -->
<section class="sign landscape landscape--upper">
  <svg class="backdrop" viewBox="0 0 540 330" preserveAspectRatio="none">
    <path d="M0,252 C120,250 200,128 282,128 C370,128 430,270 540,276 L540,330 L0,330 Z" fill="var(--green)"/>
    <path d="M0,290 C130,288 210,168 282,168 C360,168 420,300 540,306 L540,330 L0,330 Z" fill="url(#upperGrey)"/>
    <defs>
      <linearGradient id="upperGrey" x1="0" y1="0" x2="1" y2="0">
        <stop offset="0" stop-color="var(--panel-grey-a)"/>
        <stop offset="1" stop-color="var(--panel-grey-b)"/>
      </linearGradient>
    </defs>
  </svg>
  <div class="portrait tone-studio" style="left:19px;top:50px;width:156px;height:156px" role="img" aria-label="Portrait photo of a smiling woman in red"></div>
  <div class="portrait tone-garden" style="left:410px;top:18px;width:100px;height:100px" role="img" aria-label="Portrait photo of a smiling young person with glasses"></div>
  <div class="portrait tone-desert" style="left:423px;top:129px;width:86px;height:86px" role="img" aria-label="Portrait photo of a smiling woman in the desert"></div>
  <div class="portrait tone-sunset" style="left:197px;top:153px;width:150px;height:150px" role="img" aria-label="Portrait photo of a smiling woman at sunset"></div>
  <div class="brand-name">brightarc orthodontics</div>
  <p class="tagline"><span class="lead">Creating great,</span> <span class="rest">straight smiles</span></p>
</section>

<!-- Landscape sign: lower -->
<section class="sign landscape landscape--lower">
  <svg class="backdrop" viewBox="0 0 540 330" preserveAspectRatio="none">
    <defs>
      <linearGradient id="lowerGrey" x1="0" y1="0" x2="1" y2="0">
        <stop offset="0" stop-color="var(--panel-grey-a)"/>
        <stop offset="1" stop-color="var(--panel-grey-b)"/>
      </linearGradient>
    </defs>
    <path d="M0,256 C110,250 170,126 245,126 C340,126 400,278 540,278 L540,292 C400,292 330,160 245,160 C180,160 120,300 0,300 Z" fill="var(--green)"/>
    <path d="M0,296 C120,296 180,158 245,158 C330,158 400,292 540,292 L540,330 L0,330 Z" fill="var(--green)"/>
    <path d="M0,330 L0,330 Z" fill="url(#lowerGrey)"/>
    <path d="M300,116 C380,108 420,140 460,180 C490,210 515,220 540,218 C500,226 470,214 440,190 C400,158 360,128 300,116 Z" fill="var(--purple)"/>
  </svg>
  <div class="portrait tone-warm" style="left:18px;top:50px;width:156px;height:156px" role="img" aria-label="Portrait photo of a laughing woman with curly hair"></div>
  <div class="portrait tone-desert" style="left:409px;top:16px;width:100px;height:100px" role="img" aria-label="Portrait photo of a smiling woman in the desert"></div>
  <div class="portrait tone-sunset" style="left:197px;top:171px;width:150px;height:150px" role="img" aria-label="Portrait photo of a smiling woman at sunset"></div>
  <div class="brand-name">brightarc orthodontics</div>
  <p class="tagline"><span class="lead">Creating great,</span> <span class="rest">straight smiles</span></p>
</section>

</body>
</html>
```